Lantern - Web Design Project

We are seeking to have our website redesigned. Our current webpage is rather dated looking www.lantern-outcomes.com We will be utilizing similar content to explain our services as what is in the website now. We do not see it at a retail portal but rather a website for those inquiring about our services as a reference check so to speak.

We wish to have a look that is considered clean, fresh, contemporary and contains a business savvy vibe.

We prefer isolated white background and also wish to retain the integrity of our Logo and colour scheme.

We are looking for something that doesnt look like it was designed at home on sitemoose. We are hoping to find something that looks like it would reside on a tablet.
Updates

Hello designers!

We apologize for our tardiness as we have been quite preoccupied. We will be extending our invites to the end of January!

Hello All,

Please review our offer once again for updated requirements.  We are hoping to accept a design by months end.

Lantern

Target Market(s)

Business to business clients and Large manufacturers

Industry/Entity Type

Retail

Requirements
Must have
• Existing Logo

There must be an area dedicated to an intro video that will be incorporated on our landing page.

We require design of the other pages as well not only the landing page.

```html
<!DOCTYPE html>
<html lang="en">
<head>
<meta charset="utf-8">
<title>Lantern Performance Group</title>
<link rel="stylesheet" href="https://fonts.googleapis.com/css2?family=PT+Sans:ital,wght@0,400;0,700;1,400&display=swap">
<style>
:root{
  --red:#e0110f;
  --red-line:#e5403c;
  --ink:#222;
  --grey:#555;
  --nav:#444;
  --white:#fff;
}
*{margin:0;padding:0;box-sizing:border-box}
html,body{width:1200px;height:898px;overflow:hidden;background:var(--white)}
body{font-family:"PT Sans",sans-serif;color:var(--ink);position:relative;border-top:4px solid var(--red)}
.site-header{position:absolute;top:0;left:0;width:1200px;height:104px}
.logo{position:absolute;left:55px;top:22px;display:flex;align-items:center;gap:10px;font-size:56px;font-weight:400;color:var(--grey);letter-spacing:-1px}
.logo-dot{width:14px;height:14px;border-radius:50%;background:var(--red)}
.social{position:absolute;right:54px;top:20px;display:flex;gap:5px}
.social span{width:30px;height:30px;border-radius:7px;background:var(--red)}
.main-nav{position:absolute;right:60px;top:68px;display:flex;gap:28px;font-size:18px}
.main-nav a{color:var(--nav);text-decoration:none}
.main-nav a.current{color:var(--red)}
.hero{position:absolute;top:104px;left:0;width:1200px;height:486px;
  background:linear-gradient(180deg,#9fb8d6 0%,#b9cde4 45%,#d8e2ec 75%,#eef1f4 100%);
  border-top:1px solid #bbb;border-bottom:3px solid var(--red-line)}
.hero-quote{position:absolute;left:656px;top:24px;width:481px;height:199px;background:rgba(255,255,255,.6);padding:24px 29px}
.hero-quote p{font-style:italic;font-size:19px;line-height:29px;color:#333}
.hero-quote cite{display:block;margin-top:8px;font-style:normal;font-size:21px;color:#222}
.content{position:absolute;top:590px;left:0;width:1200px}
.col h2{font-weight:400;font-size:22px;color:var(--red);margin-bottom:16px}
.col p{font-size:16px;line-height:21.5px;text-align:justify;hyphens:auto}
.col-welcome{position:absolute;left:43px;top:28px;width:384px}
.col-solutions{position:absolute;left:468px;top:28px;width:318px}
.col-contact{position:absolute;left:843px;top:28px}
.contact-card{position:absolute;left:-2px;top:48px;width:312px;height:152px;background:var(--red);color:var(--white);border-radius:3px;padding:11px 20px;font-size:16px;line-height:23.5px}
.contact-card strong{font-weight:700}
.site-footer{position:absolute;top:859px;left:0;width:1200px;border-top:1px solid var(--red-line)}
.site-footer p{position:absolute;right:44px;top:12px;font-size:13px;color:#333}
</style>
</head>
<body>
<header class="site-header">
  <div class="logo"><span class="logo-dot"></span>lantern</div>
  <div class="social"><span></span><span></span><span></span></div>
  <nav class="main-nav">
    <a class="current" href="#">Home</a>
    <a href="#">Who we are</a>
    <a href="#">Cross the lantern</a>
    <a href="#">Performance Solutions</a>
    <a href="#">Sustain Solutions</a>
    <a href="#">Join us</a>
  </nav>
</header>

<section class="hero" role="img" aria-label="Photograph of a long concrete highway bridge against a blue sky with snowy mountains below">
  <blockquote class="hero-quote">
    <p>There are managers so preoccupied with their e-mail messages that they never look up from their screens to see what's happening in the nondigital world.</p>
    <cite>- Marlen Ostrova</cite>
  </blockquote>
</section>

<main class="content">
  <section class="col col-welcome">
    <h2>Welcome to Lantern Performance Group</h2>
    <p>Lantern Performance Group Inc. is the leading provider of profit generating and people development solutions. With the hands-on experience of best practices, the state-of-the-art technology and in-depth information we help companies increase their efficiencies and profits. Frank, honest, committed, valuable and rewarding are words that customers use to describe the quality services provided by Lantern Performance Group.</p>
  </section>
  <section class="col col-solutions">
    <h2>Our Solutions</h2>
    <p>Lorem ipsum dolor sit amet, diceret offendit id mea. Ne sea etiam error pericula. Ad has verterem rationibus. Ea harum ludus delectus ius, ex malis libris laboramus his, mandamus mnesarchum no pri.</p>
  </section>
  <section class="col col-contact">
    <h2>Contact us</h2>
    <address class="contact-card" style="font-style:normal">
      58 Harrow Lane,<br>
      Ottawa, ON K2P 4R8,<br>
      Canada<br>
      <strong>T :+1.888.555.0142</strong><br>
      <strong>Email:info@lantern-outcomes.com</strong>
    </address>
  </section>
</main>

<footer class="site-footer">
  <p>Copyright 2012 Lantern Performance Group. All rights reserved.</p>
</footer>
</body>
</html>
```